School Signage

I am wanting designs for signs completed that prompt students of the school requirements for hats, preparation and play.

I've uploaded rough examples of what we're after, but we would like them stylised and better than the example, including:
- A stylised logo/graphic for the 'Wallumba 1, 2, 3'
- Clear, crisp signage for the words.
- Graphics that reinforce the message of the sign.

We're after three signs:
- One that will be located on the oval to prompt hat use.
- One that will be near the entry prompting the morning routine (please make this one landscape with instructions for 'on time' on one side, and 'late' on the other).
- One that will be located within the school prompting readiness for class.

```html
<!DOCTYPE html>
<html lang="en">
<head>
<meta charset="utf-8">
<title>Wallumba 1.2.3 School Signage</title>
<link href="https://fonts.googleapis.com/css2?family=Lilita+One&family=Nunito:ital,wght@0,800;0,900;1,700;1,800;1,900&family=Allura&display=swap" rel="stylesheet">
<style>
:root{
  --stage:#474747;
  --green:#2a6549;
  --green-dark:#245a40;
  --green-olive:#5f8e34;
  --yellow:#ffc20e;
  --yellow-soft:#f6c93a;
  --yellow-bright:#ffe800;
  --amber:#f4bf45;
  --white:#ffffff;
  --title-yellow:#ffc800;
}
*{box-sizing:border-box;margin:0;padding:0}
html,body{width:1200px;height:600px;overflow:hidden;background:var(--stage)}
.canvas{position:relative;width:1200px;height:600px}
.sign{position:absolute;top:52px;width:350px;height:498px;overflow:hidden;box-shadow:0 4px 14px rgba(0,0,0,.35)}
.sign--routine{left:41px;background:linear-gradient(160deg,#ffd21a,var(--yellow) 60%,#f7b500)}
.sign--ready{left:425px;background:var(--yellow-soft)}
.sign--hats{left:809px;background:var(--amber)}
.sign svg.backdrop{position:absolute;inset:0;width:350px;height:498px}
.abs{position:absolute}
.title{font-family:"Lilita One",sans-serif;line-height:1;text-align:center;transform:rotate(-5deg);white-space:nowrap}
.title--white{color:var(--white)}
.title--yellow{color:var(--title-yellow);text-shadow:0 2px 0 rgba(0,0,0,.12)}
.num{font-family:"Lilita One",sans-serif;color:var(--title-yellow);font-size:46px;line-height:1;transform:rotate(-5deg);text-shadow:0 2px 0 rgba(0,0,0,.12)}
.heading{font-family:"Nunito",sans-serif;font-style:italic;font-weight:900;font-size:12px;color:var(--green);text-decoration:underline}
.step{font-family:"Nunito",sans-serif;font-style:italic;font-weight:800;font-size:9.6px;line-height:1.35;color:var(--green);display:flex;align-items:center;gap:5px}
.step--right{justify-content:flex-end;text-align:right}
.icon{flex:none;width:17px;height:17px;border-radius:4px}
.motto{font-family:"Allura",cursive;color:var(--green);font-size:29px;line-height:.85;transform:rotate(-14deg);text-align:center;white-space:nowrap}
.item{font-family:"Nunito",sans-serif;font-style:italic;font-weight:800;font-size:18px;line-height:1.2;color:var(--title-yellow);display:flex;align-items:center;gap:12px}
.item .icon{width:26px;height:26px;border-radius:6px}
.pill{position:absolute;background:var(--white);border-radius:0 14px 14px 0;color:var(--green);font-family:"Nunito",sans-serif;line-height:1}
.brand{position:absolute;width:36px;display:flex;flex-direction:column;align-items:center;gap:2px}
.brand__mark{width:26px;height:26px;border-radius:50%;background:var(--green-dark);border:2px solid var(--yellow)}
.brand__name{font-family:"Nunito",sans-serif;font-weight:800;font-size:5.5px;color:var(--green-dark);white-space:nowrap}
</style>
</head>
<body>
<main class="canvas">

  <section class="sign sign--routine">
    <svg class="backdrop" viewBox="0 0 350 498" aria-hidden="true">
      <defs>
        <radialGradient id="mottoGlow" cx=".5" cy=".5" r=".5">
          <stop offset="0" stop-color="#fff6c4" stop-opacity=".75"/>
          <stop offset="1" stop-color="#fff6c4" stop-opacity="0"/>
        </radialGradient>
      </defs>
      <path fill="#2a6549" d="M0 0 H256 C300 40 305 100 282 132 C250 172 160 160 100 175 C62 185 48 220 46 260 C44 320 58 380 60 430 C60 460 45 485 30 498 H0 Z"/>
      <ellipse cx="195" cy="310" rx="130" ry="70" fill="url(#mottoGlow)"/>
    </svg>
    <div class="abs title title--white" style="left:20px;top:45px;font-size:25px;width:240px">Morning Routine</div>
    <div class="abs title title--yellow" style="left:10px;top:74px;font-size:33px;width:270px">The Wallumba</div>
    <div class="abs num" style="left:92px;top:95px">1.2.3</div>

    <div class="abs heading" style="left:83px;top:170px">ON TIME:</div>
    <div class="abs" style="left:79px;top:190px;display:flex;flex-direction:column;gap:6px">
      <div class="step"><span class="icon" role="img" aria-label="Clock icon" style="background:#e6a800;border-radius:50%"></span>Arrive before 8:30 AM</div>
      <div class="step"><span class="icon" role="img" aria-label="Lockers icon" style="background:#7aa6d8"></span>Drop bag at locker and<br>collect learning materials</div>
      <div class="step"><span class="icon" role="img" aria-label="Backpack icon" style="background:#f08a2c"></span>Arrive at Home Group /<br>House Assembly before 8:40 AM</div>
    </div>

    <div class="abs motto" style="left:105px;top:283px;width:180px">Early is on time,<br>on time is late!</div>

    <div class="abs heading" style="right:26px;top:338px">RUNNING LATE:</div>
    <div class="abs" style="right:24px;top:356px;display:flex;flex-direction:column;gap:7px;align-items:flex-end">
      <div class="step step--right">Arrive before 8:30 AM<span class="icon" role="img" aria-label="School building icon" style="background:#e2683a"></span></div>
      <div class="step step--right">Drop bag at locker and<br>collect learning materials<span class="icon" role="img" aria-label="Lockers icon" style="background:#7aa6d8"></span></div>
      <div class="step step--right">Arrive at Home Group /<br>House Assembly before 8:40 AM<span class="icon" role="img" aria-label="Assembly group icon" style="background:#8b6fd0"></span></div>
    </div>

    <div class="pill" style="left:66px;top:451px;width:150px;height:31px;padding:4px 0 0 10px">
      <div style="font-weight:800;font-size:10.5px">EXCEED YOUR</div>
      <div style="font-weight:900;font-style:italic;font-size:16px">EXPECTATION</div>
    </div>
    <div class="brand" style="left:28px;top:446px"><span class="brand__mark"></span><span class="brand__name">Wallumba SHS</span></div>
  </section>

  <section class="sign sign--ready">
    <svg class="backdrop" viewBox="0 0 350 498" aria-hidden="true">
      <defs>
        <linearGradient id="readyGreen" x1="0" y1="0" x2="0" y2="1">
          <stop offset="0" stop-color="#5f8e34"/>
          <stop offset=".45" stop-color="#2a6549"/>
          <stop offset="1" stop-color="#265e44"/>
        </linearGradient>
      </defs>
      <path fill="url(#readyGreen)" d="M90 0 H262 C300 60 292 120 306 172 C320 232 280 262 300 332 C320 402 272 432 305 498 H62 C110 450 40 400 46 330 C52 262 92 232 56 172 C22 112 68 60 90 0 Z"/>
    </svg>
    <div class="abs title title--white" style="left:40px;top:52px;font-size:21px;width:260px">Are you ready for class?</div>
    <div class="abs title title--yellow" style="left:32px;top:78px;font-size:36px;width:280px">The Wallumba</div>
    <div class="abs num" style="left:124px;top:110px">1.2.3</div>

    <div class="abs" style="left:55px;top:186px;display:flex;flex-direction:column;gap:28px">
      <div class="item"><span class="icon" role="img" aria-label="Laptop icon" style="background:#3fa3e0"></span>Laptop/workbook</div>
      <div class="item"><span class="icon" role="img" aria-label="Phone pouch icon" style="background:#1ea38a"></span>Phone in Pocketlock</div>
      <div class="item"><span class="icon" role="img" aria-label="School cap icon" style="background:#f2b92a;border-radius:50%"></span>Correct uniform<br>(including hat)</div>
    </div>

    <div class="pill" style="left:56px;top:449px;width:244px;height:34px;padding:5px 0 0 12px">
      <div style="font-weight:900;font-size:17.5px;letter-spacing:.3px">CURIOSITY AND DRIVE</div>
      <div style="font-weight:800;font-size:10px;letter-spacing:.6px;margin-top:1px">WALLUMBA LEARNER VALUES</div>
    </div>
    <div class="brand" style="left:20px;top:446px"><span class="brand__mark"></span><span class="brand__name">Wallumba SHS</span></div>
  </section>

  <section class="sign sign--hats">
    <svg class="backdrop" viewBox="0 0 350 498" aria-hidden="true">
      <defs>
        <linearGradient id="hatsYellow" x1="0" y1="0" x2="0" y2="1">
          <stop offset="0" stop-color="#ffee00"/>
          <stop offset="1" stop-color="#f4c21a"/>
        </linearGradient>
      </defs>
      <rect width="180" height="498" fill="url(#hatsYellow)"/>
      <path fill="#2a6549" d="M78 0 H280 C292 60 275 120 268 175 C260 240 245 290 245 350 C245 410 270 460 300 498 H80 C100 440 110 390 110 340 C110 290 60 260 42 200 C28 140 60 60 78 0 Z"/>
    </svg>
    <div class="abs" style="left:88px;top:32px;transform:rotate(-5deg);font-family:'Lilita One',sans-serif;color:var(--white);line-height:1;text-align:center;width:210px">
      <div><span style="font-size:19px">We wear </span><span style="font-size:30px">HATS</span></div>
      <div style="font-size:21px;margin-top:-1px">at Wallumba</div>
      <div style="margin-top:2px"><span style="font-size:18px">When </span><span style="font-size:26px">OUTDOORS..</span></div>
    </div>
    <div class="abs title title--yellow" style="left:62px;top:112px;font-size:34px;width:270px">The Wallumba</div>
    <div class="abs num" style="left:140px;top:145px">1.2.3</div>

    <div class="abs" style="left:120px;top:220px;display:flex;flex-direction:column;gap:34px">
      <div class="item"><span class="icon" role="img" aria-label="Walking figure icon" style="background:#4f9a68"></span>Walking</div>
      <div class="item"><span class="icon" role="img" aria-label="Sitting figure icon" style="background:#4f9a68"></span>Sitting</div>
      <div class="item"><span class="icon" role="img" aria-label="Playing figure icon" style="background:#4f9a68"></span>Playing</div>
    </div>

    <div class="pill" style="left:66px;top:451px;width:124px;height:32px;padding:7px 0 0 10px">
      <div style="font-weight:900;font-style:italic;font-size:18px;letter-spacing:.4px">INTEGRITY</div>
    </div>
    <div class="brand" style="left:28px;top:446px"><span class="brand__mark"></span><span class="brand__name">Wallumba SHS</span></div>
  </section>

</main>
</body>
</html>
```